Banner ad to sell prefabricated holiday homes in New Zealand

Harbourlight Homes build prefabricated homes in a factory that are then transported by truck to their site. It's coming into summer here in New Zealand and many people will be thinking about the holidays and wishing they had a holiday home.

The design should communicate some of the following benefits of our homes:
- Full project management
- Great value for money
- Delivered complete with all interior & exterior fittings
- Quality construction in our controlled factory

The banner ad will be displayed on a popular weather website www.skyreport.co.nz
Size: 760px x 120px
Would like it to be animated if but the size must be below 60kb.

I'll upload some nice holiday destination photos for backgrounds & some pictures of our holiday home designs for you to use.
Our main company colors are bright blue (pantone 3005) and light grey/silver.

Updatefor brief:
I would like the animation to show different text so that it's not all squashed up on the one image.
For example have "Prefabricated Holiday Homes" on one image & then it fades/changes to next image with "Delivered complete with all interior & exterior fittings". Or something like that with nice background images or pictures of our houses.

Font styles to use
Sans Serif

Colors
3176b5
0d5aa6
33a6d7
3276b5

Requirements
Nice to have
• Our logo

```html
<!DOCTYPE html>
<html lang="en">
<head>
<meta charset="utf-8">
<title>Harbourlight Homes – Prefabricated Holiday Homes Banner</title>
<link rel="stylesheet" href="https://fonts.googleapis.com/css2?family=Libre+Baskerville:wght@400;700&display=swap">
<style>
  :root {
    --brand-blue: #33a6d7;
    --brand-white: #ffffff;
    --ink-dark: #1f2226;
    --page-bg: #eceff1;
    --sky: #a9bccb;
    --hills: #8a7b55;
    --pasture: #6f8f4a;
    --cladding: #3e5670;
    --deck: #b59366;
  }
  html, body {
    margin: 0;
    padding: 0;
    width: 1200px;
    height: 900px;
    overflow: hidden;
    background: var(--page-bg);
  }
  .banner {
    position: absolute;
    left: 220px;
    top: 390px;
    width: 760px;
    height: 120px;
    overflow: hidden;
    font-family: "Libre Baskerville", Georgia, serif;
  }
  .banner-shapes {
    position: absolute;
    inset: 0;
    display: block;
  }
  .headline {
    position: absolute;
    left: 0;
    top: 16px;
    width: 172px;
    margin: 0;
    color: var(--brand-white);
    font-size: 15.5px;
    font-weight: 700;
    line-height: 29px;
    text-align: center;
  }
  .benefit {
    position: absolute;
    left: 532px;
    top: 24px;
    margin: 0;
    color: var(--brand-white);
    font-size: 14.5px;
    font-weight: 700;
    line-height: 17px;
  }
  .brand {
    position: absolute;
    left: 524px;
    top: 90px;
    display: flex;
    align-items: center;
    gap: 10px;
  }
  .brand-mark {
    width: 22px;
    height: 22px;
    background: var(--brand-blue);
  }
  .brand-name {
    color: var(--ink-dark);
    font-size: 16px;
    font-weight: 700;
    white-space: nowrap;
  }
</style>
</head>
<body>
  <div class="banner">
    <svg class="banner-shapes" viewBox="0 0 760 120" width="760" height="120" aria-hidden="false">
      <defs>
        <linearGradient id="scene-tones" x1="0" y1="0" x2="0" y2="1">
          <stop offset="0" stop-color="var(--sky)"/>
          <stop offset="0.22" stop-color="var(--hills)"/>
          <stop offset="0.38" stop-color="var(--pasture)"/>
          <stop offset="0.5" stop-color="var(--cladding)"/>
          <stop offset="0.82" stop-color="var(--cladding)"/>
          <stop offset="1" stop-color="var(--deck)"/>
        </linearGradient>
      </defs>
      <rect class="home-photo" x="150" y="0" width="400" height="120" fill="url(#scene-tones)"
            role="img" aria-label="Photo of a blue weatherboard prefabricated holiday home with a veranda, set before New Zealand mountains"/>
      <polygon class="panel-left" points="0,0 200,0 158,120 0,120" fill="var(--brand-blue)"/>
      <polygon class="panel-right" points="536,0 760,0 760,85 503,85" fill="var(--brand-blue)"/>
      <polygon class="brand-strip" points="503,85 760,85 760,120 490,120" fill="var(--brand-white)"/>
    </svg>

    <h1 class="headline">Prefabricated<br>Holiday Homes In<br>New Zealand</h1>
    <p class="benefit">Delivered complete with all<br>interior &amp; exterior fittings</p>

    <div class="brand">
      <span class="brand-mark"></span>
      <span class="brand-name">Harbourlight Homes</span>
    </div>
  </div>
</body>
</html>
```